WP website design for Belcourt

We need a wordpress design for an established auction and real estate company based in New Jersey. The winning design will incorporate a professional color scheme with company logo in a clean layout. The design needs to consider that this will be developed on a responsive theme. Colors are those that will highlight the logo

Industry/Entity Type

Real Estate

Font styles to use
Serif
Sans Serif

Requirements
Must have
• colors will be #3E3D5D and #3C7296
navigation: 1) Home 2) Auctions 3) Real Estate Listings 4) Buyers 5) Sellers 6) About Us 7 ) Contact Us
design will use a slideshow - image is attached.
Widgets to place in the header, sidebar or footer:
1) email signup form 2) social icons (facebook, twitter, youtube, RSS) 3) Featured Properties widget 4) Featured Auctions widget 5) News & Events blog 6) Featured Videos
Nice to have
• Site will have numerous dropdown menus - so it would be nice to have a sample of what the dropdowns would look like. EG 1)▪ Our Featured Listings and 2)▪ MLS Property Search under the main "Real Estate Listings" menu item.

```html
<!DOCTYPE html>
<html lang="en">
<head>
<meta charset="utf-8">
<title>Belcourt Real Estate &amp; Auction</title>
<link rel="stylesheet" href="https://fonts.googleapis.com/css2?family=Open+Sans:wght@400;600&display=swap">
<style>
:root{
  --navy:#3E3D5D;
  --blue:#3C7296;
  --text:#666;
  --muted:#999;
  --price:#a3282b;
  --line:#ddd;
  --band:#f1f1f1;
  --footer:#2c2c2c;
  --footer-base:#232323;
  --footer-head:#7fa9c9;
  --white:#fff;
}
*{box-sizing:border-box;margin:0;padding:0}
html,body{width:708px;height:1200px;overflow:hidden}
body{font-family:"Open Sans",Arial,sans-serif;color:var(--text);background:#fcfcfc;position:relative}
h1,h2,h3{font-weight:400}
.abs{position:absolute}
ul{list-style:none}

/* header */
.brand{left:60px;top:14px;display:flex;flex-direction:column;gap:4px}
.brand-mark{width:40px;height:40px;background:var(--navy)}
.brand-name{font-size:17px;font-weight:600;color:var(--navy);letter-spacing:.5px;line-height:1}
.brand-tag{font-size:6.5px;font-weight:600;color:var(--navy);letter-spacing:.2px}
.search{left:349px;top:24px;width:92px;height:18px;border:1px solid #d8d8d8;background:var(--white);font-size:7.5px;color:#aaa;padding:4px 6px}
.search svg{position:absolute;right:4px;top:3px}
.btn{top:24px;height:18px;font-size:7.5px;font-weight:600;color:var(--white);display:flex;align-items:center;justify-content:center;border-radius:2px}
.btn-register{left:445px;width:49px;background:var(--navy)}
.btn-login{left:498px;width:39px;background:var(--blue)}
.social{top:23px;width:20px;height:20px;border-radius:2px}
.social-a{left:543px;background:#3b5b99}
.social-b{left:572px;background:#2ea6dd}
.social-c{left:601px;background:#f29122}
.social-d{left:629px;background:#d8d8d8;border:1px solid #bbb}
.nav{top:73px;left:0;width:708px;height:12px;font-size:7.7px;color:#808080;text-transform:uppercase}
.nav li{position:absolute;top:0}
.nav .active{color:var(--navy);font-weight:600}
.dropdown{left:302px;top:94px;width:119px;height:41px;background:var(--navy);padding:8px 0 0 8px;font-size:7.3px;color:var(--white);font-weight:600}
.dropdown li{margin-bottom:5px}
.dropdown li::before{content:"• "}
.dropdown-caret{left:352px;top:89px;width:0;height:0;border-left:5px solid transparent;border-right:5px solid transparent;border-bottom:5px solid var(--navy)}

/* slider */
.slide{left:0;top:97px;width:708px;height:278px;background:linear-gradient(180deg,#9cc3e6 0%,#dfe9f1 38%,#4f8a2e 58%,#2f7a1e 100%)}
.slide-caption{left:0;top:342px;width:708px;text-align:center;font-size:14px;color:var(--white);letter-spacing:.3px}
.slide-arrow{top:226px;width:22px;height:20px;background:#d9d9d9;display:flex;align-items:center;justify-content:center}

/* welcome */
.welcome-title{left:0;top:398px;width:708px;text-align:center;font-size:14.5px;color:var(--navy)}
.welcome-text{left:96px;top:420px;width:516px;text-align:center;font-size:7.4px;line-height:13.6px}
.rule{height:1px;background:var(--line)}

.section-title{font-size:14px;color:var(--navy);text-transform:uppercase;font-weight:400}
.more{width:10px;height:10px;border-radius:50%;background:#c4c4c4}
.more::after{content:"";position:absolute;left:4px;top:3px;border-left:3px solid var(--white);border-top:2px solid transparent;border-bottom:2px solid transparent}

.card{width:135px}
.card-photo{width:135px;height:75px}
.card-name{margin:10px 0 0 3px;font-size:8.8px;color:var(--blue);text-transform:uppercase;font-weight:400}
.card-desc{margin:3px 0 0 3px;font-size:6.8px;line-height:10px;color:#888}
.card-price{margin:3px 0 0 3px;font-size:8px;color:var(--price)}

.box{border:1px solid var(--line);background:var(--white)}
.blog-item{position:relative;padding-left:25px;padding-right:8px;font-size:7.6px;line-height:12.5px;color:var(--blue)}
.blog-item::before{content:"›";position:absolute;left:10px;top:-1px;color:#aaa;font-size:10px}
.blog-date{display:block;color:#999;font-size:7px;margin-top:3px}
.badge{background:#e4e4e4;border:1px solid #bcbcbc}

/* videos */
.videos{left:0;top:890px;width:708px;height:126px;background:var(--band)}
.videos-title{left:0;top:908px;width:708px;text-align:center}
.video{top:938px;width:92px;height:60px;display:flex;align-items:center;justify-content:center}
.play{width:18px;height:18px;border-radius:50%;background:rgba(20,20,20,.8);position:relative}
.play::after{content:"";position:absolute;left:7px;top:5px;border-left:6px solid var(--white);border-top:4px solid transparent;border-bottom:4px solid transparent}

/* footer */
.footer{left:0;top:1016px;width:708px;height:148px;background:var(--footer)}
.footer-base{left:0;top:1164px;width:708px;height:36px;background:var(--footer-base);font-size:7px;color:#888;text-align:center;line-height:38px}
.footer-col{top:1031px;font-size:7.5px;color:#ddd;font-weight:400}
.footer-col h3{font-size:9.5px;font-weight:400;color:var(--footer-head);margin-bottom:8px}
.footer-col li{line-height:14.8px}
.news li{padding-left:11px;position:relative;line-height:11px;margin-bottom:13px;width:170px;font-weight:400}
.news li::before{content:"•";position:absolute;left:0}
.news .date{display:block;color:#999;font-size:6.8px;margin-top:4px}
.signup p{color:#bbb;line-height:11px;width:150px;margin-bottom:6px}
.field{width:145px;height:16px;background:#eee;border:1px solid #ccc;border-radius:2px;font-size:7px;color:#555;padding:3px 8px;margin-bottom:4px}
.subscribe{left:597px;top:1124px;width:49px;height:17px;background:var(--blue);border:1px solid #6b9cc0;border-radius:2px;color:var(--white);font-size:7px;display:flex;align-items:center;justify-content:center}
</style>
</head>
<body>

<header>
  <div class="abs brand">
    <span class="brand-mark"></span>
    <span class="brand-name">BELCOURT</span>
    <span class="brand-tag">REAL ESTATE &amp; AUCTION</span>
  </div>
  <div class="abs search">Search
    <svg width="10" height="10" viewBox="0 0 10 10"><circle cx="4" cy="4" r="3" fill="none" stroke="#999" stroke-width="1.3"/><line x1="6.3" y1="6.3" x2="9.3" y2="9.3" stroke="#999" stroke-width="1.5"/></svg>
  </div>
  <a class="abs btn btn-register">REGISTER</a>
  <a class="abs btn btn-login">LOG IN</a>
  <span class="abs social social-a" aria-label="Social profile link"></span>
  <span class="abs social social-b" aria-label="Social profile link"></span>
  <span class="abs social social-c" aria-label="News feed link"></span>
  <span class="abs social social-d" aria-label="Video channel link"></span>

  <ul class="abs nav">
    <li style="left:210px">Home</li>
    <li style="left:258px">Auctions</li>
    <li class="active" style="left:321px">Real Estate Listings</li>
    <li style="left:429px">Buyers</li>
    <li style="left:482px">Sellers</li>
    <li style="left:537px">About Us</li>
    <li style="left:599px">Contact Us</li>
  </ul>
</header>

<section>
  <div class="abs slide" role="img" aria-label="Farm landscape with green field, barns and silos under a cloudy sky"></div>
  <div class="abs slide-arrow" style="left:0"><svg width="10" height="12"><path d="M8 1 2 6l6 5" fill="none" stroke="#555" stroke-width="2"/></svg></div>
  <div class="abs slide-arrow" style="left:686px"><svg width="10" height="12"><path d="M2 1l6 5-6 5" fill="none" stroke="#555" stroke-width="2"/></svg></div>
  <p class="abs slide-caption">VESTIBULUM EGESTAS ODIO NEC ANTE ULTRICES CONDIMENTUM</p>
</section>

<span class="abs dropdown-caret"></span>
<ul class="abs dropdown">
  <li>OUR FEATURED LISTINGS</li>
  <li>REAL ESTATE LISTINGS</li>
</ul>

<section>
  <h1 class="abs welcome-title">WELCOME TO BELCOURT REAL ESTATE &amp; ACTION</h1>
  <p class="abs welcome-text">Duis quis blandit elit. Curabitur scelerisque sapien sed enim consectetur condimentum. In velit nisl, venenatis nec odio eget, rutrum condimentum nibh. Aliquam erat volutpat. Praesent rhoncus a diam a luctus. Mauris fringilla, purus nec luctus scelerisque, justo velit vehicula risus, sit amet ultricies mi tortor ut dolor. Vivamus sit amet libero eget lorem ullamcorper rhoncus sed sed diam.</p>
</section>
<div class="abs rule" style="left:59px;top:486px;width:590px"></div>

<!-- featured properties -->
<h2 class="abs section-title" style="left:59px;top:508px">Featured Properties</h2>
<span class="abs more" style="left:484px;top:513px"></span>
<article class="abs card" style="left:60px;top:534px">
  <div class="card-photo" role="img" aria-label="Two-storey family house with garden" style="background:linear-gradient(180deg,#6fa6df,#c9a877 60%,#4f7d3a)"></div>
  <h3 class="card-name">Property Name</h3><p class="card-desc">Sed fermentum interdum felis, nec tempus felis sodales eget.</p><p class="card-price">$0000.00</p>
</article>
<article class="abs card" style="left:210px;top:534px">
  <div class="card-photo" role="img" aria-label="City skyline over water at sunset" style="background:linear-gradient(180deg,#a9bdd0,#e9d2b0 55%,#7d7567)"></div>
  <h3 class="card-name">Property Name</h3><p class="card-desc">Sed fermentum interdum felis, nec tempus felis sodales eget.</p><p class="card-price">$0000.00</p>
</article>
<article class="abs card" style="left:359px;top:534px">
  <div class="card-photo" role="img" aria-label="Modern apartment building with balconies" style="background:linear-gradient(135deg,#3d5fbf,#8d6b55 55%,#e2ded8)"></div>
  <h3 class="card-name">Property Name</h3><p class="card-desc">Sed fermentum interdum felis, nec tempus felis sodales eget.</p><p class="card-price">$0000.00</p>
</article>
<div class="abs rule" style="left:59px;top:688px;width:436px"></div>

<!-- featured auctions -->
<h2 class="abs section-title" style="left:59px;top:705px">Featured Auctions</h2>
<span class="abs more" style="left:484px;top:710px"></span>
<article class="abs card" style="left:60px;top:732px">
  <div class="card-photo" role="img" aria-label="Mediterranean style villa with palm trees" style="background:linear-gradient(180deg,#a6c4e4,#cdb58a 60%,#6d7a4a)"></div>
  <h3 class="card-name">Property Name</h3><p class="card-desc">Sed fermentum interdum felis, nec tempus felis sodales eget.</p><p class="card-price">$0000.00</p>
</article>
<article class="abs card" style="left:210px;top:732px">
  <div class="card-photo" role="img" aria-label="Glass office tower seen from below" style="background:linear-gradient(135deg,#1f4f99,#8fb3e0 50%,#2a5ba8)"></div>
  <h3 class="card-name">Property Name</h3><p class="card-desc">Sed fermentum interdum felis, nec tempus felis sodales eget.</p><p class="card-price">$0000.00</p>
</article>
<article class="abs card" style="left:359px;top:732px">
  <div class="card-photo" role="img" aria-label="Brick family home with front lawn" style="background:linear-gradient(180deg,#7ea9d9,#9c6a55 55%,#4d8a35)"></div>
  <h3 class="card-name">Property Name</h3><p class="card-desc">Sed fermentum interdum felis, nec tempus felis sodales eget.</p><p class="card-price">$0000.00</p>
</article>

<!-- sidebar -->
<h2 class="abs section-title" style="left:508px;top:508px">Blog</h2>
<aside class="abs box" style="left:510px;top:534px;width:137px;height:155px;padding-top:15px">
  <p class="blog-item">Donec magna ante, congue ut nunc nec, aliquam eleme ntum augue quis leo.<span class="blog-date">Aug 2, 2014</span></p>
  <p class="blog-item" style="margin-top:25px">Donec magna ante, congue ut nunc nec, aliquam eleme ntum augue quis leo.<span class="blog-date">Aug 2, 2014</span></p>
</aside>

<h2 class="abs section-title" style="left:508px;top:705px">Affiliation</h2>
<aside class="abs box" style="left:510px;top:732px;width:137px;height:130px">
  <span class="abs badge" style="left:13px;top:17px;width:25px;height:24px"></span>
  <span class="abs badge" style="left:45px;top:17px;width:65px;height:20px"></span>
  <span class="abs badge" style="left:14px;top:55px;width:68px;height:25px"></span>
  <span class="abs badge" style="left:92px;top:58px;width:28px;height:24px"></span>
</aside>

<!-- videos -->
<section>
  <div class="abs videos"></div>
  <h2 class="abs section-title videos-title">Featured Videos</h2>
  <div class="abs video" style="left:60px;background:linear-gradient(180deg,#b5c8d8,#8a8278 60%,#5e6a4a)" role="img" aria-label="Video: townhouses on a street"><span class="play"></span></div>
  <div class="abs video" style="left:159px;background:linear-gradient(180deg,#7fa3c6,#5d6b6e 55%,#4b7a2e)" role="img" aria-label="Video: suburban house with lawn"><span class="play"></span></div>
  <div class="abs video" style="left:258px;background:linear-gradient(180deg,#4f79b8,#c9c9c9 55%,#6e6e6e)" role="img" aria-label="Video: modern white house"><span class="play"></span></div>
  <div class="abs video" style="left:358px;background:linear-gradient(180deg,#3f6fbf,#c8a56a 55%,#3e7b2c)" role="img" aria-label="Video: large house with trees"><span class="play"></span></div>
  <div class="abs video" style="left:457px;background:linear-gradient(180deg,#315a9c,#6a5d5a 55%,#3a3f47)" role="img" aria-label="Video: house at dusk"><span class="play"></span></div>
  <div class="abs video" style="left:557px;background:linear-gradient(180deg,#a7b9c9,#e3cfae 55%,#6e6a60)" role="img" aria-label="Video: skyline over water"><span class="play"></span></div>
</section>

<!-- footer -->
<footer>
  <div class="abs footer"></div>
  <div class="abs footer-col" style="left:69px">
    <h3>Quick Links</h3>
    <ul><li>Home</li><li>Auctions</li><li>Real Estate Listings</li><li>Buyers</li><li>Sellers</li><li>About Us</li><li>Contact Us</li></ul>
  </div>
  <div class="abs footer-col" style="left:184px">
    <h3>Support Links</h3>
    <ul><li>Clients</li><li>Partners</li><li>Testimonials</li><li>Jobs</li><li>Categories</li></ul>
  </div>
  <div class="abs footer-col news" style="left:301px">
    <h3>Latest News &nbsp;&amp; Evetns</h3>
    <ul>
      <li>Nullam sed faucibus lectus. Sed aliquet vestibulum ipsum<span class="date">Aug 3, 2014</span></li>
      <li>Nullam sed faucibus lectus. Sed aliquet vestibulum ipsum<span class="date">Aug 3, 2014</span></li>
    </ul>
  </div>
  <div class="abs footer-col signup" style="left:502px">
    <h3>Newsletters Sign Up</h3>
    <p>Sign up for our daily email by entering your information below</p>
    <div class="field">Your name</div>
    <div class="field">Email address</div>
  </div>
  <div class="abs subscribe">SUBSCRIBE</div>
  <div class="abs footer-base">Copyright &copy; 2014 &nbsp;Belcourt Real Estate &amp; Action. &nbsp;All rights reserved.</div>
</footer>

</body>
</html>
```